Boutique Soy Candle Company Needs a Label Design

We need a label design for a boutique soy candle company based in Kestrel Bay, South Australia.
We sell high quality, hand poured soy wax candles, melts and reed diffusers.
We are based in a coastal town and would like the label to reflect our rustic, beachy, retro but luxurious feel. I've attached the design we've been using and like the idea but want to have something more professional. The picture of the Venner Spire is something that we would like to be included somehow - it's like our town symbol - a 'lighthouse' of sorts. It was quite stylised on my original design but we are open to different interpretations.
We like the idea of a 'Kraft' brown paper sort of label but are not set on it. We also love the fluro pink look.

```html
<!DOCTYPE html>
<html lang="en">
<head>
<meta charset="utf-8">
<title>Lumen Soy Candle Co. — Honey Suckle Jasmine Label</title>
<link href="https://fonts.googleapis.com/css2?family=Alfa+Slab+One&family=Montserrat:wght@700;800&display=swap" rel="stylesheet">
<style>
  :root {
    --backdrop: #3d3d3d;
    --paper: #ffffff;
    --fluro-pink: #e5007f;
    --shadow-pink: #b8006a;
    --ornament-tint: #f3a6cf;
  }
  * { margin: 0; padding: 0; box-sizing: border-box; }
  html, body {
    width: 1200px;
    height: 1120px;
    overflow: hidden;
    background: var(--backdrop);
  }
  .canvas {
    position: relative;
    width: 1200px;
    height: 1120px;
  }
  .label {
    position: absolute;
    left: 322px;
    top: 231px;
    width: 613px;
    height: 657px;
    background: var(--paper);
  }
  .label-frame {
    position: absolute;
    left: 0;
    top: 0;
    width: 1200px;
    height: 1120px;
  }
  .brand {
    position: absolute;
    left: 348px;
    top: 262px;
    width: 562px;
    height: 272px;
    display: flex;
    flex-direction: column;
    align-items: center;
    justify-content: center;
    gap: 14px;
    color: var(--fluro-pink);
    font-family: "Montserrat", sans-serif;
    font-weight: 800;
  }
  .brand-dot {
    width: 62px;
    height: 62px;
    border-radius: 50%;
    background: var(--fluro-pink);
  }
  .brand-name {
    font-size: 64px;
    line-height: 1;
    letter-spacing: 1px;
  }
  .brand-sub {
    font-size: 15px;
    letter-spacing: 1px;
    line-height: 1;
  }
  .scent-name {
    position: absolute;
    left: 348px;
    top: 542px;
    width: 562px;
    height: 134px;
    display: flex;
    flex-direction: column;
    align-items: center;
    justify-content: center;
    color: var(--paper);
    font-family: "Alfa Slab One", serif;
    font-size: 33px;
    line-height: 1.18;
    letter-spacing: 1.5px;
    text-shadow: 3px 3px 0 var(--shadow-pink);
    text-align: center;
  }
  .origin {
    position: absolute;
    left: 348px;
    top: 684px;
    width: 562px;
    height: 94px;
    display: flex;
    align-items: center;
    justify-content: center;
    color: var(--fluro-pink);
    font-family: "Montserrat", sans-serif;
    font-weight: 700;
    font-size: 17.5px;
    letter-spacing: 1px;
  }
  .spec {
    position: absolute;
    top: 790px;
    height: 76px;
    display: flex;
    align-items: center;
    justify-content: center;
    color: var(--paper);
    font-family: "Montserrat", sans-serif;
    font-weight: 700;
    font-size: 34px;
    letter-spacing: 1.5px;
  }
  .spec-weight { left: 344px; width: 328px; }
  .spec-number { left: 680px; width: 234px; }
</style>
</head>
<body>
<div class="canvas">
  <div class="label"></div>

  <svg class="label-frame" viewBox="0 0 1200 1120" xmlns="http://www.w3.org/2000/svg" aria-hidden="true">
    <g fill="none" stroke="var(--fluro-pink)">
      <rect x="342" y="254" width="572" height="612" stroke-width="4"/>
      <rect x="348" y="262" width="562" height="272" stroke-width="3"/>
      <rect x="348" y="684" width="562" height="94" stroke-width="3"/>
    </g>
    <g fill="var(--fluro-pink)">
      <rect x="348" y="542" width="562" height="134"/>
      <rect x="344" y="790" width="328" height="76"/>
      <rect x="680" y="790" width="234" height="76"/>
      <!-- brand panel corners -->
      <path d="M356 270 h22 a22 22 0 0 0 -22 22 z"/>
      <path d="M902 270 h-22 a22 22 0 0 1 22 22 z"/>
      <path d="M356 526 h22 a22 22 0 0 1 -22 -22 z"/>
      <path d="M902 526 h-22 a22 22 0 0 0 22 -22 z"/>
      <!-- origin panel corners -->
      <path d="M356 692 h18 a18 18 0 0 0 -18 18 z"/>
      <path d="M902 692 h-18 a18 18 0 0 1 18 18 z"/>
      <path d="M356 770 h18 a18 18 0 0 1 -18 -18 z"/>
      <path d="M902 770 h-18 a18 18 0 0 0 18 -18 z"/>
    </g>
    <g fill="var(--paper)">
      <!-- scent band corners -->
      <path d="M356 550 h18 a18 18 0 0 0 -18 18 z"/>
      <path d="M902 550 h-18 a18 18 0 0 1 18 18 z"/>
      <path d="M356 668 h18 a18 18 0 0 1 -18 -18 z"/>
      <path d="M902 668 h-18 a18 18 0 0 0 18 -18 z"/>
    </g>
    <rect x="590" y="686" width="78" height="12" fill="var(--ornament-tint)" role="img" aria-label="Small decorative flourish"/>
    <rect x="590" y="762" width="78" height="12" fill="var(--ornament-tint)" role="img" aria-label="Small decorative flourish"/>
  </svg>

  <header class="brand">
    <span class="brand-dot"></span>
    <span class="brand-name">Lumen</span>
    <span class="brand-sub">SOY CANDLE CO.</span>
  </header>

  <h1 class="scent-name"><span>HONEY</span><span>SUCKLE JASMINE</span></h1>

  <p class="origin">HANDMADE IN KESTREL BAY, SOUTH AUSTRALIA</p>

  <p class="spec spec-weight">300 GRAMS</p>
  <p class="spec spec-number">NO.004</p>
</div>
</body>
</html>
```